Tamaru Peruvian Cuisine needs a take-out menu

We need a new tri-fold 8.5"x11" take out menu for a Peruvian restaurant based in New Rochelle, NY. We have a vast selections of dishes from appetizers, seafood based dishes, desserts, Peruvian ceviches and more. We have attached the following:

Restaurant information
Pictures of our dishes
Tamaru Logo in pdf format
Menu in word format
Old take out menu for reference only! (our dishes have changed)
Updates

Project Deadline Extended
Reason: Need more time to make final decision.

Industry/Entity Type

Restaurant

```html
<!DOCTYPE html>
<html lang="en">
<head>
<meta charset="utf-8">
<title>Tamaru Peruvian Cuisine – Take-out Menu</title>
<link href="https://fonts.googleapis.com/css2?family=Oswald:wght@500;600&family=Open+Sans:wght@400;600;700&family=Italianno&display=swap" rel="stylesheet">
<style>
:root{
  --bg:#e9e9e9;
  --wood-dark:#4e240f;
  --wood:#7a3d1b;
  --paper:#efe0bb;
  --paper-dark:#dcc391;
  --white-paper:#f7f4ec;
  --green:#2fae55;
  --green-dark:#1d7d3a;
  --green-text:#3f9a2f;
  --heading:#6e2710;
  --ink:#3a2414;
  --yellow:#f4e64c;
  --cream:#fff8e0;
}
*{box-sizing:border-box;margin:0;padding:0}
html,body{width:848px;height:1200px;overflow:hidden;background:var(--bg)}
body{position:relative;font-family:"Open Sans",sans-serif;color:var(--ink)}
.sheet{position:absolute;left:44px;width:760px;height:580px;display:flex;box-shadow:0 4px 14px rgba(0,0,0,.35)}
.sheet--outside{top:12px}
.sheet--inside{top:608px}
.panel{width:253.34px;height:100%;position:relative;overflow:hidden}
.wood{background:linear-gradient(90deg,var(--wood-dark),var(--wood) 20%,#5e2d12 50%,var(--wood) 80%,var(--wood-dark))}
.paper-sheet{background:linear-gradient(160deg,var(--paper),var(--paper-dark))}
.white-sheet{background:linear-gradient(180deg,#fff,var(--white-paper) 60%,var(--paper))}
.green-sheet{background:linear-gradient(90deg,#2a9d4a,var(--green) 50%,#279446);color:#fff}
.paper-insert{position:absolute;left:9px;right:9px;top:12px;bottom:14px;background:linear-gradient(165deg,var(--paper),var(--paper-dark));box-shadow:0 2px 6px rgba(0,0,0,.4)}

.brand-badge{display:flex;align-items:center;justify-content:center;gap:6px;width:136px;height:44px;margin:0 auto;border-radius:50%;background:var(--cream);border:3px solid var(--green)}
.brand-badge .dot{width:9px;height:9px;border-radius:50%;background:var(--green)}
.brand-badge .name{font-family:"Oswald",sans-serif;font-weight:500;font-size:14px;color:var(--green-dark);letter-spacing:1px}
.brand-badge--sm{width:96px;height:30px;border-width:2px}
.brand-badge--sm .name{font-size:10px}

.section-title{display:flex;align-items:center;justify-content:center;gap:6px;font-family:"Oswald",sans-serif;font-weight:600;font-size:15px;color:var(--heading);letter-spacing:.3px;margin:6px 0 4px}
.section-title::before,.section-title::after{content:"";width:30px;height:1.5px;background:currentColor}
.green-sheet .section-title{color:var(--yellow)}
.green-sheet .section-title::before,.green-sheet .section-title::after{background:#fff}

.menu{padding:0 10px}
.item{display:grid;grid-template-columns:1fr auto;column-gap:6px;margin-bottom:5px}
.item-name{font-size:6.6px;font-weight:700;text-transform:uppercase;white-space:nowrap;overflow:hidden}
.item-name::after{content:" ......................................................................................................................";font-weight:400}
.price{font-size:9.5px;font-weight:700;line-height:1;text-align:right;grid-row:span 2}
.desc{font-size:6px;line-height:1.3;color:var(--green-text);grid-column:1}
.options{grid-column:1/3;display:flex;gap:6px;align-items:flex-start}
.options .desc{flex:1}
.opts{border-left:1.2px solid var(--ink);border-radius:4px 0 0 4px;padding-left:4px;font-size:6.2px;line-height:1.5;display:grid;grid-template-columns:auto auto;column-gap:10px;min-width:86px}
.opts b{font-size:9.5px;text-align:right}
.green-sheet .item-name,.green-sheet .desc{color:#fff}
.green-sheet .price{color:var(--yellow)}
.white-sheet .desc{color:#4a8a2c}

.photo{background:radial-gradient(circle at 45% 45%,#c86a3a,#6b2e17 60%,#3c1a0c);border:4px solid #fff;outline:3px solid var(--green);border-radius:50%}
.website{font-family:"Italianno",cursive;font-size:16px;letter-spacing:1.5px;text-align:center;color:var(--green-dark)}
.tagline{font-family:"Italianno",cursive;font-size:22px;color:var(--green-dark);text-align:center;line-height:1}
.brand-word{font-family:"Oswald",sans-serif;font-weight:500;font-size:40px;color:var(--green-dark);text-align:center;line-height:1;letter-spacing:2px}

/* outside – contact panel */
.contact{position:absolute;left:0;right:0;top:418px;text-align:center;color:#fff}
.contact .note{font-size:10.4px;font-weight:600;line-height:1.35;padding:0 10px}
.call{display:inline-block;margin-top:4px;padding:1px 10px;border:1px solid var(--yellow);border-radius:10px;font-family:"Oswald",sans-serif;font-size:11px;color:var(--yellow);letter-spacing:.5px}
.hours-title{font-size:10px;font-weight:700;color:#5ee07a;margin-top:3px}
.hours{font-size:8px}
.address{font-family:"Italianno",cursive;font-size:14px;color:var(--yellow);border-top:1px solid var(--yellow);border-bottom:1px solid var(--yellow);margin:4px 18px 0;padding:1px 0}
.contact .website{color:#fff;font-size:12px;margin-top:6px}

.green-splash{position:absolute;border-radius:40% 55% 45% 50%;background:var(--green)}
.pill-opts{display:flex;gap:12px;font-size:7px;font-weight:700;color:var(--yellow);padding-left:40px;margin-top:1px}
.pill-opts span::before{content:"";display:inline-block;width:5px;height:5px;border-radius:50%;background:#d42424;margin-right:3px}
.ceviche-opts{display:grid;grid-template-columns:auto auto;gap:0 16px;font-size:6.8px;font-weight:600;border-left:1.2px solid var(--yellow);border-right:1.2px solid var(--yellow);border-radius:5px;padding:1px 6px;margin:2px 0 4px}
</style>
</head>
<body>

<!-- OUTSIDE -->
<section class="sheet sheet--outside">
  <div class="panel wood">
    <div class="paper-insert">
      <div style="padding-top:8px"><div class="brand-badge"><span class="dot"></span><span class="name">Tamaru</span></div></div>
      <h2 class="section-title">APPETIZERS</h2>
      <div class="menu">
        <div class="item"><div class="item-name">Chicharron de Calamares</div><div class="price">12.95</div><p class="desc">crispy fried calamari served with house tartar sauce and salsa criolla</p></div>
        <div class="item"><div class="item-name">Anticucho Carretillero</div><div></div>
          <div class="options"><p class="desc">choice chicken or cow's heart Peruvian style kebabs, served with Cusco corn and grilled potatoes</p><div class="opts"><span>Corazon –</span><b>15.95</b><span>Pollo –</span><b>15.95</b></div></div></div>
        <div class="item"><div class="item-name">Palta Rellena</div><div></div>
          <div class="options"><p class="desc">peruvian avocado stuffed with choice of chicken or shrimp, marinated in Peruvian spices</p><div class="opts"><span>Camarones –</span><b>11.95</b><span>Pollo –</span><b>8.95</b></div></div></div>
        <div class="item"><div class="item-name">Tamal Criollo</div><div class="price">5.95</div><p class="desc">peruvian chicken tamale, served with salsa criolla</p></div>
        <div class="item"><div class="item-name">Salchipapa</div><div class="price">9.95</div><p class="desc">french fries mixed with sliced hot dogs</p></div>
        <div class="item"><div class="item-name">Papa a la Huancaina</div><div class="price">8.95</div><p class="desc">boiled potatoes, topped with ají amarillo and queso fresco sauce, egg, olives</p></div>
        <div class="item"><div class="item-name">Ocopa Arequipeña</div><div class="price">8.95</div><p class="desc">boiled potatoes, topped with ají amarillo and queso fresco sauce, egg, olives</p></div>
        <div class="item"><div class="item-name">Empanada Limeña</div><div class="price">3.95</div><p class="desc">patties stuffed with choice of chicken or beef</p></div>
        <div class="item"><div class="item-name">Causa</div><div></div>
          <div class="options"><p class="desc">cold mashed potato infused with key of lime juice, pressed into a cake with choice of chicken or shrimp</p><div class="opts"><span>Camarones –</span><b>9.95</b><span>Pollo –</span><b>7.95</b></div></div></div>
        <div class="item"><div class="item-name">Choritos a la Chalaca</div><div class="price">10.95</div><p class="desc">steamed mussels topped with diced onions, tomatoes, lime juice and Cusco corn</p></div>
        <div class="item"><div class="item-name">Piqueo Tamaru</div><div class="price">19.95</div><p class="desc">Dished combined of Chicharron de Calamares, Papa a la Huancaina, Choritos a la Chalaca and Causa</p></div>
      </div>
    </div>
  </div>

  <div class="panel white-sheet">
    <h2 class="section-title" style="margin-top:12px">SALADS</h2>
    <div class="menu">
      <div class="item"><div class="item-name">Ensalada de la Casa</div><div class="price">6.95</div><p class="desc">lettuce, tomatoes, yellow peppers and zucchini</p></div>
      <div class="item"><div class="item-name">Ensalada Tamaru</div><div class="price">7.95</div><p class="desc">lettuce, tomatoes, cucumbers, red onions, carrots, radish and avocado</p></div>
      <div class="item"><div class="item-name">Ensalada Cesar</div><div class="price">8.95</div><p class="desc">romaine, lettuce, croutons, parmesan cheese and Tamaru's special sauce</p></div>
    </div>
    <h2 class="section-title">SOUPS</h2>
    <div class="menu">
      <div class="item"><div class="item-name">Aguadito Limeño</div><div></div>
        <div class="options"><p class="desc">chicken and vegetable soup mixed with rice and cilantro</p><div class="opts" style="min-width:70px;font-size:5.8px"><span>Large –</span><span>9.95</span><span>Small –</span><span>5.95</span></div></div></div>
      <div class="item"><div class="item-name">Sopa a la Minuta</div><div class="price">12.95</div><p class="desc">traditional milk and angel's hair pasta soup, served with beef and eggs</p></div>
      <div class="item"><div class="item-name">Caldo de Gallina</div><div class="price">12.95</div><p class="desc">hen broth with noodles, scallion, potatoes and hard-boiled egg</p></div>
      <div class="item"><div class="item-name">Chupe de Camarones Arequipeño</div><div class="price">15.95</div><p class="desc">shrimp soup mixed with rice, green peas, Cusco corn, milk, eggs and Peruvian spices</p></div>
    </div>
    <div class="green-splash" style="left:-6px;right:-6px;top:368px;height:110px;background:var(--green)"></div>
    <div style="position:absolute;left:0;right:0;top:380px">
      <div class="brand-word" style="color:var(--yellow)">Tamaru</div>
      <div class="tagline" style="color:var(--wood-dark)">Authentic Peruvian Cuisine</div>
    </div>
    <div style="position:absolute;left:0;right:0;top:504px"><div class="brand-badge brand-badge--sm"><span class="dot"></span><span class="name">Tamaru</span></div></div>
    <div class="website" style="position:absolute;left:0;right:0;bottom:8px">www.tamarunewrochelle.com</div>
  </div>

  <div class="panel wood">
    <div style="position:absolute;left:0;right:0;top:0;height:200px;background:linear-gradient(180deg,var(--paper),var(--paper-dark))"></div>
    <div style="position:relative;padding-top:20px"><div class="brand-badge"><span class="dot"></span><span class="name">Tamaru</span></div></div>
    <div class="brand-word" style="position:relative;margin-top:6px">Tamaru</div>
    <div class="tagline" style="position:relative">Authentic Peruvian Cuisine</div>
    <div class="photo" role="img" aria-label="Photo of lomo saltado with beef, tomato, onion and white rice" style="position:absolute;left:-6px;top:150px;width:250px;height:250px"></div>
    <div class="contact">
      <p class="note">Deliveries on order of $15 or more, $5 fee for 3 miles or more Chef's specials on weekends.</p>
      <div class="call">CALL US NOW: 914-555-0172</div>
      <div class="hours-title">Delivery Hours:</div>
      <div class="hours">Mon – Sun 11:30 am – 10 pm</div>
      <div class="address">218 Harbor Ave, New Rochelle, NY 10801</div>
      <div class="website">www.tamarunewrochelle.com</div>
    </div>
  </div>
</section>

<!-- INSIDE -->
<section class="sheet sheet--inside">
  <div class="panel green-sheet">
    <h2 class="section-title" style="margin-top:10px">CEVICHES</h2>
    <div class="menu">
      <div class="item"><div class="item-name">Chicharron de Calamares</div><div class="price">10.95</div><p class="desc">ceviche marinade in fresh lime juice</p></div>
      <div class="item"><div class="item-name">Tiradito en Salsa de Ají Amarillo</div><div class="price">12.95</div><p class="desc">sashimi style fish in yellow pepper sauce and fresh lime juice, served with Cusco corn and sweet potatoes</p></div>
      <div class="item"><div class="item-name">Piqueo Chalaco</div><div class="price">24.95</div><p class="desc">dish combined of Ceviche de Pescado (Fish Ceviche) and Jalea (Fried Seafood)</p></div>
      <div class="item" style="margin-bottom:0"><div class="item-name">Ceviche</div><div></div><p class="desc" style="grid-column:1/3">choice of raw fish, mixed seafood, shrimp or shrimp with octopus, marinated in fresh lime juice, with red onions, Cusco corn and sweet potatoes</p></div>
      <div class="ceviche-opts"><span>Pescado – 15.95</span><span>Camaron – 17.95</span><span>Mixto – 17.95</span><span>Camaron con Pulpo – 18.95</span></div>
    </div>
    <h2 class="section-title" style="margin-top:2px">SIDES</h2>
    <div class="menu">
      <div class="item"><div class="item-name">Papas Fritas</div><div class="price">3.95</div><p class="desc">french fries</p></div>
      <div class="item"><div class="item-name">Arroz Blanco o Amarillo</div><div class="price">3.95</div><p class="desc">white/yellow rice</p></div>
      <div class="item"><div class="item-name">Frejoles</div><div class="price">3.95</div><p class="desc">peruvian canario beans</p></div>
      <div class="item"><div class="item-name">Maduros</div><div class="price">3.95</div><p class="desc">sweet plantains</p></div>
      <div class="item"><div class="item-name">Tostones</div><div class="price">3.95</div><p class="desc">fried green plantains</p></div>
      <div class="item"><div class="item-name">Yuca Frita</div><div class="price">3.95</div><p class="desc">fried yuccas</p></div>
    </div>
    <h2 class="section-title">SEAFOOD</h2>
    <div class="menu">
      <div class="item"><div class="item-name">Pescado a lo Macho</div><div class="price">19.95</div><p class="desc">fried fish fillet topped with seafood in hot yellow pepper sauce, served with rice and yuccas</p></div>
      <div class="item"><div class="item-name">Pescado Sudado</div><div class="price">16.95</div><p class="desc">corvina fish stew, in hot yellow pepper, tomatoes, onions, served with yuccas and rice</p></div>
      <div class="item"><div class="item-name">Arroz con Mariscos</div><div class="price">17.95</div><p class="desc">peruvian style paella, red rice served with seafood</p></div>
      <div class="item" style="margin-bottom:2px"><div class="item-name">Arroz Chaufa</div><div class="price">17.95</div><p class="desc">peruvian style fried rice served with choice of seafood or shrimp</p></div>
      <div class="pill-opts"><span>Mariscos</span><span>Camarones</span></div>
      <div class="item" style="margin-top:4px"><div class="item-name">Trucha Frita</div><div class="price">18.95</div><p class="desc">deep fried Trout, served with white rice, fried</p></div>
      <div class="item"><div class="item-name">Jalea</div><div></div><p class="desc" style="grid-column:1/3">deep fried mixed seafood and fish, served with fried yuccas<br><b>Large – 28.95 | Small – 17.95</b></p></div>
    </div>
  </div>

  <div class="panel wood">
    <div class="paper-insert" style="top:14px;bottom:26px">
      <h2 class="section-title" style="margin-top:8px">TRADITIONAL DISHES</h2>
      <div class="menu">
        <div class="item"><div class="item-name">Parrillada Mixta</div><div class="price">30.95</div><p class="desc">dish combined of grilled NY Strip steak, anticuchos (Peruvian style kebabs), pork chops and sausage</p></div>
        <div class="item"><div class="item-name">Churrasco en Salsa de Camarones</div><div class="price">20.95</div><p class="desc">NY strip steak topped with shrimps on hot yellow pepper sauce, served with rice</p></div>
        <div class="item"><div class="item-name">Seco Norteño</div><div class="price">20.95</div><p class="desc">slowly cooked lamb stew in ají panka sauce, served with rice and Peruvian canario beans</p></div>
        <div class="item"><div class="item-name">Seco de Pato Piurano</div><div class="price">17.95</div><p class="desc">slowly cooked duck stew in ají panka sauce, served with rice and hard-boiled yuccas</p></div>
        <div class="item"><div class="item-name">Tallarines Verdes con Churrasco</div><div class="price">18.95</div><p class="desc">linguine pasta in Peruvian style pesto sauce served with grilled NY Strip steak</p></div>
        <div class="item"><div class="item-name">Tacu Tacu</div><div></div>
          <div class="options"><p class="desc">peruvian canario beans mixed with rice, served with choice of NY Strip or wosered beef in soy sauce</p><div class="opts" style="min-width:76px;font-size:5.8px"><span>Churrasco –</span><span>18.95</span><span>Pollo –</span><span>15.95</span></div></div></div>
        <div class="item"><div class="item-name">Churrasco a lo Pobre</div><div class="price">19.95</div><p class="desc">NY Strip steak served with fried eggs, sweet plantains, French fries and rice</p></div>
        <div class="item"><div class="item-name">Saltado</div><div></div>
          <div class="options"><p class="desc">choice of wok-seared steak or chicken, mixed with red onions, tomatoes, in soy sauce, served with French fries and rice</p><div class="opts" style="min-width:68px;font-size:5.8px"><span>Lomo –</span><span>15.95</span><span>Pollo –</span><span>13.95</span></div></div></div>
        <div class="item"><div class="item-name">Aeropuerto</div><div class="price">18.95</div><p class="desc">peruvian style fried rice, mixed with noodles, chicken, beef and shrimp</p></div>
        <div class="item"><div class="item-name">Seco de Carne</div><div class="price">15.95</div><p class="desc">beef ribs stew in ají panka sauce, served with with rice and Peruvian canario beans</p></div>
        <div class="item"><div class="item-name">Ají de Gallina</div><div class="price">11.95</div><p class="desc">shredded chicken in a spicy ají amarillo creamy sauce, hard-boiled egg, olives, potatoes and rice</p></div>
        <div class="item"><div class="item-name">Arroz Chaufa</div><div></div>
          <div class="options"><p class="desc">peruvian style fried rice mixed with choice of beef or chicken</p><div class="opts" style="min-width:66px;font-size:5.8px"><span>Carne –</span><span>14.95</span><span>Pollo –</span><span>12.95</span></div></div></div>
      </div>
    </div>
    <div style="position:absolute;left:28px;top:498px"><div class="brand-badge brand-badge--sm"><span class="dot"></span><span class="name">Tamaru</span></div></div>
    <div class="photo" role="img" aria-label="Photo of fish ceviche with red onion" style="position:absolute;right:8px;top:488px;width:62px;height:62px;background:radial-gradient(circle,#f2ece0,#d9c6a6 60%,#b08060)"></div>
    <div class="website" style="position:absolute;left:0;right:0;bottom:4px;color:#fff;font-size:14px">www.tamarunewrochelle.com</div>
  </div>

  <div class="panel white-sheet">
    <h2 class="section-title" style="margin-top:14px">CHICKEN</h2>
    <div class="menu">
      <div class="item"><div class="item-name">1/4 Pollo</div><div class="price">6.50</div><p class="desc">quarter chicken, served with two sides</p></div>
      <div class="item"><div class="item-name">1/2 Pollo</div><div class="price">8.95</div><p class="desc">half chicken, served with two sides</p></div>
      <div class="item"><div class="item-name">1 Pollo</div><div class="price">16.95</div><p class="desc">whole chicken, served with two sides</p></div>
      <div class="item"><div class="item-name">Pollo Limeño</div><div class="price">20.95</div><p class="desc">whole chicken, served with French fries, avocado salad and yellow rice</p></div>
      <div class="item"><div class="item-name">Pollo Chalaco</div><div class="price">26.95</div><p class="desc">whole chicken, served with avocado salad, salchipapa and yellow rice</p></div>
      <div class="item"><div class="item-name">Pollo Tamaru</div><div class="price">30.95</div><p class="desc">whole chicken, served with avocado salad, arroz chaufa (chicken or steak) and salchipapa</p></div>
    </div>
    <h2 class="section-title" style="margin-top:10px">DESSERTS</h2>
    <div class="menu">
      <div class="item"><div class="item-name">Crema Volteada</div><div class="price">5.95</div><p class="desc">Peruvian caramel custard</p></div>
      <div class="item"><div class="item-name">Tres Leches</div><div class="price">5.95</div><p class="desc">Butter cake soaked in three kinds of milk</p></div>
      <div class="item"><div class="item-name">Torta Helada</div><div class="price">5.95</div><p class="desc">Sponge cake topped with strawberry jello</p></div>
      <div class="item"><div class="item-name">Torta de Chocolate</div><div class="price">5.95</div><p class="desc">Chocolate cake</p></div>
      <div class="item"><div class="item-name">Picarones</div><div class="price">5.95</div><p class="desc">Peruvian style sweet potato doughnut covered with syrup</p></div>
    </div>
    <div class="green-splash" style="left:-10px;right:-10px;top:452px;bottom:-20px"></div>
    <div class="photo" role="img" aria-label="Photo of fried seafood platter" style="position:absolute;left:4px;top:452px;width:104px;height:104px"></div>
    <div class="photo" role="img" aria-label="Photo of creamy seafood soup" style="position:absolute;left:92px;top:400px;width:72px;height:72px;background:radial-gradient(circle,#f6e3b0,#e2b860 60%,#b57a30)"></div>
    <div class="photo" role="img" aria-label="Photo of layered causa with yellow sauce" style="position:absolute;left:96px;top:478px;width:76px;height:76px;background:radial-gradient(circle,#f5d24a,#e39a2a 60%,#a7561e)"></div>
    <div class="photo" role="img" aria-label="Photo of avocado stuffed with shrimp" style="position:absolute;left:176px;top:438px;width:70px;height:70px;background:radial-gradient(circle,#e9c49a,#9fb760 60%,#5a7a30)"></div>
  </div>
</section>

</body>
</html>
```